Yoga Studio - Class Timetable Flyer

We require a double sided, size DL (1/3 A4) flyer with our class timetable included.
We would like the final flyer to have.
Side A : Yoga image, logo, address, website, contact phone number, and in big font $40 Introductory Month.
Side B: Clear easy to read timetable, class descriptions and website.
Thank you.
Yours kindly,
Hilda
Colors
87d0c7
86cae7
85acd3

```html
<!DOCTYPE html>
<html lang="en">
<head>
<meta charset="utf-8">
<title>Stillwater Studio – DL Timetable Flyer</title>
<link rel="stylesheet" href="https://fonts.googleapis.com/css2?family=Arimo:wght@400;700&family=Barlow+Condensed:wght@600;700&family=Source+Sans+3:wght@300;400&display=swap">
<style>
  :root {
    --teal: #70ddd2;
    --teal-soft: #87d0c7;
    --orange: #f26f21;
    --hot: #f7941d;
    --brown: #6b4226;
    --blue: #5aa0f0;
    --navy: #2e3192;
    --green: #3aaa35;
    --ink: #000000;
    --paper: #ffffff;
    --text-dark: #222222;
    --grid-line: #c9c9c9;
    --backdrop: #e8e5e0;
    --photo-light: #eef1f2;
    --photo-mid: #c9ccce;
  }
  * { box-sizing: border-box; margin: 0; padding: 0; }
  html, body { width: 1102px; height: 1200px; overflow: hidden; }
  body { background: var(--backdrop); position: relative; font-family: "Arimo", Arial, sans-serif; }

  .flyer { position: absolute; top: 84px; width: 486px; height: 1031px; overflow: hidden; }
  .flyer--front { left: 42px; background: var(--ink); color: var(--paper); }
  .flyer--back { left: 574px; background: var(--paper); color: var(--text-dark); }
  .flyer__shapes { position: absolute; inset: 0; width: 486px; height: 1031px; }

  /* Brand */
  .brand { position: absolute; text-align: center; color: var(--teal); }
  .brand__dot { display: block; margin: 0 auto; border-radius: 50%; background: var(--teal); }
  .brand__name { display: block; font-family: "Arimo", Arial, sans-serif; font-weight: 400; line-height: 1; letter-spacing: 1px; }
  .brand__tag { display: block; font-family: "Source Sans 3", Arial, sans-serif; font-weight: 400; }

  .flyer--front .brand { left: 285px; top: 14px; width: 180px; }
  .flyer--front .brand__dot { width: 62px; height: 62px; margin-bottom: 28px; }
  .flyer--front .brand__name { font-size: 33px; }
  .flyer--front .brand__tag { font-size: 8px; letter-spacing: .5px; margin-top: 6px; color: var(--teal); }

  .flyer--back .brand { left: 0; width: 486px; top: 14px; }
  .flyer--back .brand__dot { width: 78px; height: 78px; margin-bottom: 20px; }
  .flyer--back .brand__name { font-size: 40px; }
  .flyer--back .brand__tag { font-size: 23px; letter-spacing: 1.5px; margin-top: 10px; font-weight: 300; }

  /* Front */
  .photo { position: absolute; left: 0; top: 0; }
  .offer { position: absolute; left: 23px; top: 630px; display: flex; align-items: baseline; gap: 20px; }
  .offer__price { font-family: "Barlow Condensed", sans-serif; font-weight: 700; font-size: 86px; color: var(--teal); line-height: 1; letter-spacing: -2px; }
  .offer__title { font-family: "Barlow Condensed", sans-serif; font-weight: 600; font-size: 36px; color: var(--paper); }
  .front-copy { position: absolute; left: 24px; width: 450px; font-size: 18.5px; line-height: 23px; }
  .front-copy--invite { top: 742px; }
  .front-copy--concession { top: 806px; }
  .contact-list { position: absolute; left: 23px; top: 876px; list-style: none; font-size: 18.5px; }
  .contact-list li { display: flex; align-items: center; gap: 10px; height: 30px; }
  .contact-list svg { width: 18px; height: 18px; flex: none; }
  .call { position: absolute; right: 14px; top: 974px; text-align: left; font-size: 20px; line-height: 25px; color: var(--ink); }

  /* Back */
  .timetable-title { position: absolute; left: 0; width: 486px; top: 197px; text-align: center; font-family: "Source Sans 3", Arial, sans-serif; font-size: 22px; color: var(--ink); }
  .timetable { position: absolute; left: 12px; top: 230px; display: grid; grid-template-columns: 65px repeat(7, 57px); grid-template-rows: 31px repeat(6, 51px); border-top: 1px solid var(--grid-line); border-left: 1px solid var(--grid-line); font-size: 11px; }
  .timetable > div { border-right: 1px solid var(--grid-line); border-bottom: 1px solid var(--grid-line); display: flex; align-items: center; justify-content: center; text-align: center; line-height: 13px; }
  .timetable .head, .timetable .time { background: var(--teal); color: var(--ink); }
  .timetable .time { justify-content: flex-start; padding-left: 10px; }
  .class { color: var(--paper); flex-direction: column; }
  .class b { font-weight: 400; font-size: 12px; }
  .class--hot { background: var(--hot); }
  .class--vinyasa { background: var(--brown); }
  .class--essentials { background: var(--blue); }
  .class--funky { background: var(--navy); }
  .class--yin { background: var(--green); }
  .class--yin b, .class--hot b { font-size: 13px; }

  .class-note { position: absolute; left: 41px; width: 430px; font-size: 15px; line-height: 20px; text-align: justify; color: var(--text-dark); }
  .class-note::before { content: ""; position: absolute; left: -18px; top: 6px; width: 11px; height: 11px; border: 2px solid var(--teal); border-radius: 50%; }
  .class-note__name { font-weight: 700; font-size: 18px; }
  .class-note--funky { top: 597px; } .class-note--funky .class-note__name { color: var(--navy); }
  .class-note--hot { top: 689px; } .class-note--hot .class-note__name { color: var(--hot); }
  .class-note--essentials { top: 748px; } .class-note--essentials .class-note__name { color: var(--blue); }
  .class-note--vinyasa { top: 824px; } .class-note--vinyasa .class-note__name { color: var(--brown); }
  .class-note--yin { top: 899px; } .class-note--yin .class-note__name { color: var(--green); }

  .back-web { position: absolute; left: 28px; top: 970px; display: flex; align-items: center; gap: 8px; font-size: 15px; }
  .back-web svg { width: 18px; height: 18px; }
  .back-call { position: absolute; right: 15px; top: 970px; text-align: right; font-size: 20px; line-height: 27px; color: var(--ink); }
  .back-call span { display: inline-flex; align-items: center; gap: 6px; }
  .back-call svg { width: 18px; height: 18px; }
</style>
</head>
<body>

<section class="flyer flyer--front">
  <svg class="flyer__shapes" viewBox="0 0 486 1031" aria-hidden="true">
    <path d="M0 0 H210 C120 25 45 85 0 165 Z" fill="var(--teal)"/>
    <path d="M0 160 C45 90 110 30 215 2 C140 30 80 80 18 155 Z" fill="var(--ink)"/>
    <path d="M22 128 C70 60 150 15 228 3 C150 25 85 70 28 135 Z" fill="var(--orange)"/>
    <path d="M14 145 C70 70 150 25 190 14" fill="none" stroke="var(--teal)" stroke-width="2.5"/>
    <path d="M0 1031 V1018 C150 1030 330 980 486 942 V1031 Z" fill="var(--teal)"/>
    <path d="M0 985 C110 1030 240 1030 340 1000 C240 1018 110 1018 0 996 Z" fill="var(--orange)"/>
    <path d="M40 1002 C150 1022 260 1010 330 996" fill="none" stroke="var(--teal)" stroke-width="2"/>
  </svg>

  <svg class="photo" width="486" height="660" viewBox="0 0 486 660" role="img" aria-label="Photo of a woman meditating cross-legged in a bright studio">
    <defs>
      <linearGradient id="photoTone" x1="0" y1="0" x2="1" y2="1">
        <stop offset="0" stop-color="var(--photo-light)"/>
        <stop offset="1" stop-color="var(--photo-mid)"/>
      </linearGradient>
    </defs>
    <ellipse cx="236" cy="408" rx="222" ry="224" fill="url(#photoTone)"/>
    <path d="M150 196 C260 170 420 220 458 360 C470 300 420 210 330 192 C270 180 200 184 150 196 Z" fill="var(--teal)"/>
    <path d="M60 560 C140 650 330 660 440 560 C360 640 160 640 60 560 Z" fill="var(--orange)"/>
  </svg>

  <div class="brand">
    <span class="brand__dot"></span>
    <span class="brand__name">stillwater</span>
    <span class="brand__tag">YOGA · FITNESS · AQUA</span>
  </div>

  <div class="offer">
    <span class="offer__price">$40</span>
    <span class="offer__title">Introductory Month</span>
  </div>
  <p class="front-copy front-copy--invite">Come &amp; Join Stillwater Yoga, Fitness Today &amp; Avail Great Discount for the first time members</p>
  <p class="front-copy front-copy--concession">Please present concession card and ID for concession prices. Available to full-time students only</p>

  <ul class="contact-list">
    <li><svg viewBox="0 0 18 18"><path d="M9 1a6 6 0 0 0-6 6c0 4.5 6 10 6 10s6-5.5 6-10a6 6 0 0 0-6-6zm0 8.5a2.5 2.5 0 1 1 0-5 2.5 2.5 0 0 1 0 5z" fill="var(--paper)"/></svg>42 Wattle Grove, Lakeside Vic 3999</li>
    <li><svg viewBox="0 0 18 18"><rect x="1" y="4" width="16" height="11" fill="var(--paper)"/><path d="M1 4 L9 10 L17 4" fill="none" stroke="var(--ink)" stroke-width="1.4"/></svg>hildamarsh@mail.com</li>
    <li><svg viewBox="0 0 18 18" fill="none" stroke="var(--paper)" stroke-width="1.3"><circle cx="9" cy="9" r="7.5"/><ellipse cx="9" cy="9" rx="3.5" ry="7.5"/><path d="M1.5 9h15M3 5h12M3 13h12"/></svg>www.stillwaterstudio.com.au</li>
  </ul>

  <div class="call">Call Us Today<br>0400-555-182</div>
</section>

<section class="flyer flyer--back">
  <svg class="flyer__shapes" viewBox="0 0 486 1031" aria-hidden="true">
    <path d="M0 0 H190 C110 30 40 90 0 165 Z" fill="var(--teal)"/>
    <path d="M0 165 C40 95 105 35 200 3 C130 35 70 85 12 160 Z" fill="var(--paper)"/>
    <path d="M18 118 C70 55 145 12 230 2 C150 22 85 65 24 126 Z" fill="var(--orange)"/>
    <path d="M8 150 C60 80 140 30 180 18" fill="none" stroke="var(--teal)" stroke-width="2.5"/>
    <path d="M0 1031 V1000 C150 1010 330 990 486 945 V1031 Z" fill="var(--teal)"/>
    <path d="M0 980 C100 1040 230 1020 330 990 C240 1015 110 1025 0 990 Z" fill="var(--orange)"/>
    <path d="M20 992 C150 1020 300 990 486 938" fill="none" stroke="var(--teal)" stroke-width="2"/>
  </svg>

  <div class="brand">
    <span class="brand__dot"></span>
    <span class="brand__name">stillwater</span>
    <span class="brand__tag">YOGA · FITNESS · AQUA</span>
  </div>

  <h2 class="timetable-title">Our Class Time Table</h2>

  <div class="timetable">
    <div class="head"></div><div class="head">Mon</div><div class="head">Tues</div><div class="head">Wed</div><div class="head">Thurs</div><div class="head">Fri</div><div class="head">Sat</div><div class="head">Sun</div>

    <div class="time">09:30am</div><div></div>
    <div class="class class--hot"><b>Hot</b>90 mins</div><div></div>
    <div class="class class--vinyasa"><b>Power Vinyasa</b>75 mins</div><div></div>
    <div class="class class--vinyasa"><b>Power Vinyasa</b>90 mins</div><div></div>

    <div class="time">11:00 AM</div><div></div><div></div><div></div>
    <div class="class class--essentials"><b>Power Essentials</b>60 mins</div><div></div><div></div><div></div>

    <div class="time">01:00pm</div><div></div><div></div>
    <div class="class class--hot"><b>Hot</b>90 mins</div><div></div><div></div><div></div><div></div>

    <div class="time">4:30 PM</div><div></div><div></div><div></div><div></div><div></div><div></div>
    <div class="class class--vinyasa"><b>Power Vinyasa</b>60 mins</div>

    <div class="time">6:30 PM</div>
    <div class="class class--vinyasa"><b>Power Vinyasa</b>60 mins</div><div></div>
    <div class="class class--hot"><b>Hot</b>90 mins</div><div></div>
    <div class="class class--funky"><b>*Funky Flow</b>75 mins</div><div></div>
    <div class="class class--yin"><b>Yin</b>60 mins</div>

    <div class="time">7:45 PM</div>
    <div class="class class--essentials"><b>Power Essentials</b>60 mins</div><div></div>
    <div class="class class--vinyasa"><b>Power Vinyasa</b>60 mins</div><div></div><div></div><div></div><div></div>
  </div>

  <p class="class-note class-note--funky"><span class="class-note__name">Funky Flow*</span>- Finish off the week and head into the week-end with a joyful flowing class to a playlist of funky beats. Charity class by donation, suggested $10. Please place cash only in the charity donation box. Frequent guest</p>
  <p class="class-note class-note--hot"><span class="class-note__name">Hot</span> - Dynamic sequence of Strength and Breathing exercises. Suitable for beginners. Heat 37 = degrees.</p>
  <p class="class-note class-note--essentials"><span class="class-note__name">Power Essentials</span> - Flowing Practice with space and time to Align and understand the poses deeply, building muscular strength and endurance. Ideal for beginners.</p>
  <p class="class-note class-note--vinyasa"><span class="class-note__name">Power Vinyasa</span> - Strong, Dynamic, Flowing practice ideal for building physical power, flexibility and mental resilience. Heat = 30 degrees</p>
  <p class="class-note class-note--yin"><span class="class-note__name">Yin</span> - Long, Slow, Deep practice with a focus on supporting the body to release our deep internal structures of connective tissue.</p>

  <div class="back-web">
    <svg viewBox="0 0 18 18" fill="none" stroke="var(--text-dark)" stroke-width="1.3"><circle cx="9" cy="9" r="7.5"/><ellipse cx="9" cy="9" rx="3.5" ry="7.5"/><path d="M1.5 9h15M3 5h12M3 13h12"/></svg>
    www.stillwaterstudio.com.au
  </div>
  <div class="back-call">Get In Today<br>
    <span><svg viewBox="0 0 18 18"><circle cx="9" cy="9" r="8" fill="none" stroke="var(--ink)" stroke-width="1.3"/><path d="M6.5 4.5 L8 7 L7 8 C7.5 9.5 8.5 10.5 10 11 L11 10 L13.5 11.5 L12.5 13.5 C9 13.5 4.5 9 4.5 5.5 Z" fill="var(--ink)"/></svg>0400-555-182</span>
  </div>
</section>

</body>
</html>
```